Brightmere Capital Design
Business Card
Brightmere Capital Design -
Creative Brief
Professional
Brightmere Capital
Loan Consultant
472 Larkin Avenue Suite 215 San Mateo CA 94403
nora@brightmerecapital.example
www.noravesko.example
DRE 04627158
aslo include license "NMLS 517904"

```html
<!DOCTYPE html>
<html lang="en">
<head>
<meta charset="utf-8">
<title>Brightmere Capital Stationery</title>
<link href="https://fonts.googleapis.com/css2?family=Open+Sans:wght@400;600;700&display=swap" rel="stylesheet">
<style>
:root{
  --bg:#e9e9ea;
  --paper:#ffffff;
  --blue:#1f63b8;
  --blue-deep:#0f3f86;
  --blue-light:#5d9be0;
  --navy:#1b3566;
  --ink:#5a5f66;
  --muted:#9aa1aa;
  --faint:#e4ecf6;
}
*{box-sizing:border-box;margin:0;padding:0}
html,body{width:1200px;height:1083px;overflow:hidden}
body{background:var(--bg);font-family:"Open Sans",Arial,sans-serif;color:var(--ink);position:relative}
.brand{display:flex;align-items:center;gap:8px;font-weight:700;color:var(--navy);white-space:nowrap}
.brand-dot{width:22px;height:22px;border-radius:50%;background:var(--blue);flex:none}
.brand--light{color:#fff}
.brand--light .brand-dot{background:#fff}

/* letterhead */
.letterhead{position:absolute;left:44px;top:111px;width:594px;height:934px;background:var(--paper);box-shadow:0 4px 14px rgba(0,0,0,.18);padding:36px 46px;overflow:hidden}
.letterhead .brand{font-size:26px}
.letterhead .brand-dot{width:30px;height:30px}
.letter-meta{margin-top:56px;font-size:11px;line-height:1.55}
.salutation{margin-top:22px;font-size:11px}
.letter-body{width:440px}
.letter-body p{font-size:9.5px;line-height:1.6;margin-top:14px;color:var(--muted);text-align:justify}
.closing{margin-top:70px;font-size:10px}
.signature{display:block;margin-top:10px;width:70px;height:38px;background:linear-gradient(90deg,#cfd3d8,#eef0f2);border-radius:4px}
.signer{font-size:9px;margin-top:6px;color:var(--muted)}
.faint-circle{position:absolute;left:100px;top:540px;width:330px;height:330px;border-radius:50%;border:46px solid var(--faint);z-index:0}
.letterhead > *:not(.faint-circle){position:relative;z-index:1}
.letter-footer{position:absolute !important;left:46px;right:46px;bottom:30px;display:flex;justify-content:flex-end;gap:24px;font-size:8px;line-height:1.6;border-top:1px solid #e2e5ea;padding-top:10px}
.letter-footer dl{display:grid;grid-template-columns:auto auto;column-gap:8px}
.letter-footer dt{color:var(--navy);font-weight:600}

/* envelope */
.envelope-back{position:absolute;left:410px;top:73px;width:700px;height:230px;background:var(--paper);box-shadow:0 4px 12px rgba(0,0,0,.16);overflow:hidden}
.envelope-back svg{position:absolute;inset:0}
.envelope-front{position:absolute;left:572px;top:250px;width:585px;height:300px;background:var(--paper);box-shadow:0 5px 16px rgba(0,0,0,.2);padding:30px 30px}
.envelope-front .brand{font-size:21px}
.envelope-front .brand-dot{width:24px;height:24px}
.envelope-address{position:absolute;right:30px;top:34px;font-size:8.5px;line-height:1.6;text-align:right;color:var(--muted)}
.envelope-band{position:absolute;left:0;right:0;bottom:0;height:10px;background:linear-gradient(90deg,var(--blue-deep),var(--blue-light))}

/* business cards */
.card{position:absolute;top:565px;width:230px;height:140px;box-shadow:0 4px 12px rgba(0,0,0,.22);overflow:hidden}
.card-front{left:655px;background:var(--paper)}
.card-band{background:linear-gradient(90deg,var(--blue-deep),var(--blue));color:#fff;padding:7px 12px;font-size:8.5px}
.card-band strong{font-weight:700}
.card-front .brand{font-size:14px;margin:12px 12px 0}
.card-front .brand-dot{width:17px;height:17px}
.card-contact{position:absolute;right:12px;bottom:10px;font-size:6.8px;line-height:1.6;text-align:right;color:var(--ink)}
.card-back{left:894px;background:radial-gradient(circle at 35% 40%,var(--blue-light),var(--blue) 55%,var(--blue-deep));display:flex;align-items:center;justify-content:center}
.card-back .brand{font-size:18px}
.card-back .brand-dot{width:19px;height:19px}

/* disc */
.disc{position:absolute;left:705px;top:715px;width:350px;height:350px}
</style>
</head>
<body>

<article class="letterhead">
  <div class="faint-circle" aria-hidden="true"></div>
  <div class="brand"><span class="brand-dot"></span>Brightmere Capital</div>
  <div class="letter-meta">Date:<br>Address:<br>Company:</div>
  <p class="salutation">Dear Martin,</p>
  <div class="letter-body">
    <p>We appreciate your interest in our lending services and are pleased to share a summary of the options available for your upcoming property purchase in San Mateo.</p>
    <p>Our team reviews each application with care, compares rates from trusted lenders, and explains every term so you can make a confident and informed decision.</p>
    <p>Please find the requested documents enclosed. Should you have any questions about closing costs, timelines or rate locks, our consultants are available throughout the week.</p>
    <p>Thank you for choosing us. We look forward to helping you reach your goals.</p>
  </div>
  <p class="closing">Your Sincerely</p>
  <span class="signature" role="img" aria-label="Handwritten signature"></span>
  <p class="signer">Elena Park</p>
  <footer class="letter-footer">
    <div>472 Larkin Avenue Suite 215<br>San Mateo CA 94403</div>
    <dl><dt>Toll Free</dt><dd>650 555 0142</dd><dt>Phone</dt><dd>650 555 0187</dd><dt>Fax</dt><dd>650 555 0199</dd></dl>
    <div>www.noravesko.example<br>DRE 04627158<br>NMLS 517904</div>
  </footer>
</article>

<section class="envelope-back" aria-label="Envelope back">
  <svg viewBox="0 0 700 230" width="700" height="230">
    <defs>
      <linearGradient id="flapGrad" x1="0" y1="0" x2="1" y2="0">
        <stop offset="0" stop-color="#0f3f86"/><stop offset=".5" stop-color="#1f63b8"/><stop offset="1" stop-color="#5d9be0"/>
      </linearGradient>
    </defs>
    <path d="M0 0 H700 V40 Q350 120 0 40 Z" fill="url(#flapGrad)"/>
    <text x="350" y="30" text-anchor="middle" fill="#fff" font-size="12" letter-spacing="3" font-family="Open Sans, sans-serif">www.noravesko.example</text>
  </svg>
</section>

<section class="envelope-front" aria-label="Envelope front">
  <div class="brand"><span class="brand-dot"></span>Brightmere Capital</div>
  <div class="envelope-address">472 Larkin Avenue Suite 215<br>San Mateo CA 94403<br>nora@brightmerecapital.example<br>www.noravesko.example</div>
  <div class="envelope-band"></div>
</section>

<section class="card card-front" aria-label="Business card front">
  <div class="card-band"><strong>Nora Vesko</strong> | Loan Consultant</div>
  <div class="brand"><span class="brand-dot"></span>Brightmere Capital</div>
  <div class="card-contact">472 Larkin Avenue Suite 215 San Mateo CA 94403<br>nora@brightmerecapital.example<br>www.noravesko.example<br>DRE 04627158 · NMLS 517904</div>
</section>

<section class="card card-back" aria-label="Business card back">
  <div class="brand brand--light"><span class="brand-dot"></span>Brightmere Capital</div>
</section>

<svg class="disc" viewBox="0 0 380 380" aria-label="Disc label">
  <defs>
    <radialGradient id="discGrad" cx=".45" cy=".4" r=".65">
      <stop offset="0" stop-color="#5d9be0"/><stop offset=".55" stop-color="#1f63b8"/><stop offset="1" stop-color="#0f3f86"/>
    </radialGradient>
    <path id="discArc" d="M190 190 m-160 0 a160 160 0 1 1 320 0"/>
  </defs>
  <circle cx="190" cy="190" r="188" fill="url(#discGrad)"/>
  <circle cx="190" cy="190" r="48" fill="#cfd8e3"/>
  <circle cx="190" cy="190" r="20" fill="#e9e9ea"/>
  <text font-size="9" fill="#fff" letter-spacing="2" font-family="Open Sans, sans-serif">
    <textPath href="#discArc" startOffset="50%" text-anchor="middle">Mortgage and refinance solutions tailored to every client</textPath>
  </text>
  <circle cx="112" cy="290" r="9" fill="#fff"/>
  <text x="127" y="296" fill="#fff" font-size="17" font-weight="700" font-family="Open Sans, sans-serif">Brightmere Capital</text>
</svg>

</body>
</html>
```